Lantern Vigor
Basketball Fitness Training
Lantern Vigor -
Creative Brief
Modern
Doran Fisk
Health and Fitness Coach
tavmirlo@quillpost.example
www.lanternvigor.example
Youth Development Clinics Private 1 on 1 Sessions Executive Training Women's Fitness Cross Training

```html
<!DOCTYPE html>
<html lang="en">
<head>
<meta charset="utf-8">
<title>Lantern Vigor – Business Card</title>
<link rel="stylesheet" href="https://fonts.googleapis.com/css2?family=Russo+One&family=PT+Serif:ital,wght@1,700&family=Open+Sans:wght@400;600&display=swap">
<style>
  :root {
    --page-bg: #e9e6e2;
    --card-bg: #ffffff;
    --ink: #141414;
    --accent-blue: #1f3f9e;
    --accent-orange: #e8732a;
    --muted: #6b6b6b;
    --divider: #9a9a9a;
    --illustration-fill: #ecdcc9;
  }
  * { box-sizing: border-box; margin: 0; padding: 0; }
  html, body {
    width: 1200px; height: 780px; overflow: hidden;
    background: var(--page-bg);
  }
  .card {
    position: absolute; left: 80px; top: 90px;
    width: 1040px; height: 600px;
    background: var(--card-bg);
    border-radius: 36px;
    box-shadow: 0 10px 30px rgba(0,0,0,.18);
    overflow: hidden;
  }
  .edge-tab {
    position: absolute; width: 30px;
    background: var(--accent-blue);
  }
  .edge-tab--left { left: 0; top: 440px; height: 110px; border-radius: 0 10px 10px 0; }
  .edge-tab--right { right: 0; top: 230px; height: 130px; border-radius: 10px 0 0 10px; }

  .brand {
    position: absolute; left: 250px; top: 70px;
    text-align: right;
    font-family: "Russo One", sans-serif;
    color: var(--ink);
  }
  .brand__name { font-size: 76px; line-height: 1; }
  .brand__tagline { font-size: 30px; line-height: 1.2; margin-top: 2px; }

  .illustration-area {
    position: absolute; left: 150px; top: 200px;
    width: 740px; height: 150px;
    background: var(--illustration-fill);
    border-radius: 6px;
  }

  .person {
    position: absolute; left: 180px; top: 405px;
    width: 280px; text-align: right;
  }
  .person__name {
    font-family: "PT Serif", serif; font-style: italic; font-weight: 700;
    font-size: 40px; color: var(--accent-blue);
  }
  .person__role {
    font-family: "Open Sans", sans-serif; font-size: 22px;
    color: var(--accent-orange); margin-top: 10px;
  }
  .divider {
    position: absolute; left: 490px; top: 385px;
    width: 2px; height: 150px; background: var(--divider);
  }
  .contact {
    position: absolute; left: 515px; top: 395px;
    list-style: none;
    font-family: "Open Sans", sans-serif; font-size: 22px; color: var(--muted);
  }
  .contact__item { display: flex; align-items: center; gap: 14px; height: 50px; }
  .contact__icon { width: 26px; height: 26px; flex: none; }
</style>
</head>
<body>
  <main class="card">
    <span class="edge-tab edge-tab--left"></span>
    <span class="edge-tab edge-tab--right"></span>

    <div class="illustration-area" role="img" aria-label="Illustration of an arm in a blue sleeve holding a basketball"></div>

    <header class="brand">
      <h1 class="brand__name">Lantern Vigor</h1>
      <p class="brand__tagline">Basketball Fitness Training</p>
    </header>

    <section class="person">
      <h2 class="person__name">Doran Fisk</h2>
      <p class="person__role">Health and Fitness Coach</p>
    </section>

    <span class="divider"></span>

    <ul class="contact">
      <li class="contact__item">
        <svg class="contact__icon" viewBox="0 0 26 26" aria-hidden="true">
          <circle cx="13" cy="13" r="12" fill="none" stroke="var(--accent-blue)" stroke-width="2"/>
          <circle cx="13" cy="13" r="4" fill="none" stroke="var(--accent-blue)" stroke-width="2"/>
          <path d="M17 9v6a3 3 0 0 0 5 0" fill="none" stroke="var(--accent-blue)" stroke-width="2"/>
        </svg>
        <span>tavmirlo@quillpost.example</span>
      </li>
      <li class="contact__item">
        <svg class="contact__icon" viewBox="0 0 26 26" aria-hidden="true">
          <circle cx="13" cy="13" r="12" fill="var(--accent-blue)"/>
          <ellipse cx="13" cy="13" rx="5" ry="11" fill="none" stroke="#fff" stroke-width="1.5"/>
          <line x1="2" y1="13" x2="24" y2="13" stroke="#fff" stroke-width="1.5"/>
        </svg>
        <span>www.lanternvigor.example</span>
      </li>
    </ul>
  </main>
</body>
</html>
```